Cover for "ROOTED! The skill and rhythm of guiding teams through calm and delight"

My first book for a global audience of modern performance leaders needs its cover!
I am an international executive coach and I've developed a new approach to replace classic Performance Management with a natural, sustainable approach fit for human beings :) My first book is about this approach and serves two purposes: helping leaders and sparking their curiosity to learn more, and positioning myself as a thought leader in the field.
The book is built on personal experience; it is both professional and personal ("From me to You"), and I'd like to position it beyond classic categorisation.
Its cover should communicate humanness, naturalness, ease and joy, within an unmistakably business-y context. I would like to see designs that use the color yellow (but not sure it communicates the right things).
Updates

Target Market(s)

Leaders who aspire to have a positive impact and deliver results in a meaningful way

Industry/Entity Type

Consulting & Executive Coaching - Trusted Advisor

Font styles to use
Other font styles liked:
• Helvetica Neue

Colors
0094D4
00A9DD
6FCCEA
C7EBF8
E9F6FB
FFC000
F8CF3A
FAE287
FDF2CF
FEFAEE
EE7325
F08F49
F5BC92
FAE3D3
FDF4ED

Requirements
Must have
• A both-and feeling to it (see description), e.g., masculine AND feminine, business AND humanness. Power with, not power over...
Should not have
• Too much "bling" - no classic status symbol business success language

```html
<!DOCTYPE html>
<html lang="en">
<head>
<meta charset="utf-8">
<title>ROOTED! Book Cover</title>
<link rel="stylesheet" href="https://fonts.googleapis.com/css2?family=Anton&display=swap">
<style>
  :root {
    --backdrop: #ececec;
    --cover-yellow: #f9c116;
    --cover-yellow-deep: #f3b914;
    --ink-blue: #1d4386;
    --paper-white: #ffffff;
  }
  * { box-sizing: border-box; margin: 0; padding: 0; }
  html, body {
    width: 1200px;
    height: 800px;
    overflow: hidden;
    background: var(--backdrop);
  }
  .canvas {
    position: relative;
    width: 1200px;
    height: 800px;
  }
  .book-cover {
    position: absolute;
    left: 387px;
    top: 30px;
    width: 426px;
    height: 740px;
    background: linear-gradient(160deg, var(--cover-yellow) 0%, var(--cover-yellow-deep) 100%);
    overflow: hidden;
  }
  .title-word {
    position: absolute;
    left: 17px;
    top: 0;
    width: 392px;
    height: 360px;
  }
  .title-word text {
    font-family: "Anton", "Impact", sans-serif;
    fill: var(--paper-white);
  }
  .subtitle {
    position: absolute;
    right: 18px;
    top: 392px;
    text-align: right;
    font-family: "Anton", "Impact", sans-serif;
    font-weight: 400;
    font-size: 50px;
    line-height: 0.88;
    letter-spacing: 0.3px;
    color: var(--ink-blue);
    text-transform: uppercase;
    white-space: nowrap;
  }
  .subtitle span { display: block; }
  .author-name {
    position: absolute;
    right: 18px;
    top: 688px;
    font-family: "Anton", "Impact", sans-serif;
    font-weight: 400;
    font-size: 20px;
    line-height: 1;
    letter-spacing: 0.6px;
    color: var(--paper-white);
    text-transform: uppercase;
    white-space: nowrap;
  }
</style>
</head>
<body>
<main class="canvas">
  <section class="book-cover">
    <svg class="title-word" viewBox="0 0 392 360" role="img" aria-label="ROOTED!">
      <text x="0" y="330" font-size="140" textLength="392" lengthAdjust="spacingAndGlyphs">ROOTED!</text>
    </svg>
    <h1 class="subtitle">
      <span>The skill</span>
      <span>and rhythm</span>
      <span>of guiding</span>
      <span>teams through</span>
      <span>calm and</span>
      <span>delight</span>
    </h1>
    <p class="author-name">Author name goes here</p>
  </section>
</main>
</body>
</html>
```